Design my dad a new business card because his current one sucks!

I need a business card designed for my fathers home maintenance business. His customers are individuals (single moms, old people etc.) as well as the occasional business. As such it needs to be accessible to both target audiences.

The front of the card should be dark grey on yellow with the logo and contain the following information:
- Darren Whitlock
- 0488 372 915
- info@bluegumhomecare.example.au
- 0488 372 915

- ABN: 71 284 630 912
- 'Fully Insured'

The reverse should be yellow on dark grey and will have the web address:
- bluegumhomecare.example.au

And a few key services he offers:
GENERAL REPAIRS
PAINTING/TILING/
PAVING &CONCRETING
PRESSURE WASHING
ON-SITE WELDING
DECKING ADDITIONS & REPAIRS
FENCING
FULL BOND CLEANING

This will be first time the logo has been printed so you will need to come up with the best CMYK approximation of the RGB colours to make sure it is a close as possible.

```html
<!DOCTYPE html>
<html lang="en">
<head>
<meta charset="utf-8">
<title>Bluegum Home Care – Business Card</title>
<link rel="stylesheet" href="https://fonts.googleapis.com/css2?family=Open+Sans:wght@400;600;700&display=swap">
<style>
  :root {
    --backdrop: #dcdbd9;
    --card-yellow: #e3d21c;
    --card-charcoal: #2b2726;
    --ink-dark: #2b2727;
    --ink-yellow: #e3d21c;
    --card-w: 420px;
    --card-h: 240px;
  }
  * { box-sizing: border-box; margin: 0; padding: 0; }
  html, body {
    width: 1200px;
    height: 720px;
    overflow: hidden;
    background: var(--backdrop);
    font-family: "Open Sans", Arial, sans-serif;
  }
  .canvas {
    position: relative;
    width: 1200px;
    height: 720px;
  }
  .card {
    position: absolute;
    width: var(--card-w);
    height: var(--card-h);
    box-shadow: 0 2px 6px rgba(0,0,0,0.12);
  }

  /* Front */
  .card-front {
    left: 370px;
    top: 95px;
    background: var(--card-yellow);
    color: var(--ink-dark);
  }
  .brand {
    position: absolute;
    left: 20px;
    top: 24px;
    display: flex;
    align-items: center;
    gap: 10px;
  }
  .brand-mark {
    width: 26px;
    height: 26px;
    border-radius: 50%;
    background: var(--ink-dark);
  }
  .brand-name {
    font-size: 30px;
    font-weight: 700;
    letter-spacing: -0.5px;
    color: var(--ink-dark);
    line-height: 1;
  }
  .owner-name {
    position: absolute;
    left: 0;
    right: 0;
    top: 96px;
    text-align: center;
    font-size: 16px;
    font-weight: 600;
  }
  .contact-list {
    position: absolute;
    left: 0;
    right: 0;
    top: 128px;
    list-style: none;
    text-align: center;
    font-size: 10px;
    line-height: 15px;
  }
  .contact-list li {
    display: flex;
    justify-content: center;
    align-items: center;
    gap: 4px;
  }
  .contact-icon {
    width: 11px;
    height: 11px;
  }
  .insured {
    position: absolute;
    right: 20px;
    top: 160px;
    font-size: 10px;
    font-weight: 600;
  }
  .abn {
    position: absolute;
    left: 20px;
    bottom: 24px;
    font-size: 10.5px;
  }
  .abn em { font-style: italic; }

  /* Back */
  .card-back {
    left: 405px;
    top: 375px;
    background: var(--card-charcoal);
    color: var(--ink-yellow);
  }
  .service-list {
    position: absolute;
    left: 0;
    right: 0;
    top: 42px;
    list-style: none;
    text-align: center;
    font-size: 9px;
    line-height: 17.5px;
    letter-spacing: 0.2px;
    text-transform: uppercase;
  }
  .web-address {
    position: absolute;
    left: 0;
    right: 0;
    bottom: 22px;
    text-align: center;
    font-size: 17px;
    font-weight: 700;
  }
</style>
</head>
<body>
<main class="canvas">

  <section class="card card-front" aria-label="Business card front">
    <div class="brand">
      <span class="brand-mark" aria-hidden="true"></span>
      <span class="brand-name">Bluegum Home Care</span>
    </div>

    <h1 class="owner-name">Darren Whitlock</h1>

    <ul class="contact-list">
      <li>
        <svg class="contact-icon" viewBox="0 0 12 12" aria-hidden="true">
          <circle cx="6" cy="6" r="6" fill="#2b2727"/>
          <path d="M3.6 3.2c.4-.4.8-.3 1 .1l.5.9c.2.3.1.6-.2.8l-.3.2c.3.7.8 1.2 1.5 1.5l.2-.3c.2-.3.5-.4.8-.2l.9.5c.4.2.5.6.1 1-.6.6-1.5.8-2.3.3-1-.6-1.9-1.5-2.5-2.5-.5-.8-.3-1.7.3-2.3z" fill="#e3d21c"/>
        </svg>
        <span>0488 372 915</span>
      </li>
      <li>
        <svg class="contact-icon" viewBox="0 0 12 12" aria-hidden="true">
          <rect x="0" y="0" width="12" height="12" rx="2" fill="#2b2727"/>
          <rect x="2.5" y="3.5" width="7" height="5" fill="none" stroke="#e3d21c" stroke-width="0.9"/>
          <path d="M2.5 3.5 6 6.3 9.5 3.5" fill="none" stroke="#e3d21c" stroke-width="0.9"/>
        </svg>
        <span>info@bluegumhomecare.example.au</span>
      </li>
      <li>
        <svg class="contact-icon" viewBox="0 0 12 12" aria-hidden="true">
          <circle cx="6" cy="6" r="6" fill="#2b2727"/>
          <rect x="4" y="2.5" width="4" height="7" rx="0.7" fill="none" stroke="#e3d21c" stroke-width="0.9"/>
          <circle cx="6" cy="8.2" r="0.5" fill="#e3d21c"/>
        </svg>
        <span>0488 372 915</span>
      </li>
    </ul>

    <p class="insured">Fully Insured</p>
    <p class="abn"><em>ABN:</em> 71 284 630 912</p>
  </section>

  <section class="card card-back" aria-label="Business card back">
    <ul class="service-list">
      <li>General Repairs</li>
      <li>Painting/Tiling/</li>
      <li>Paving &amp;Concreting</li>
      <li>Pressure Washing</li>
      <li>On-Site Welding</li>
      <li>Decking Additions &amp; Repairs</li>
      <li>Fencing</li>
      <li>Full Bond Cleaning</li>
    </ul>
    <p class="web-address">www.bluegumhomecare.example.au</p>
  </section>

</main>
</body>
</html>
```